Velvet Glow Co. Derma Roller packaging design

I need a box designed for a skin care brand called Velvet Glow Co. The box will be for our Derma Roller- a skin rejuvenation device. It will be sold online with lots of competition. I would like a modern, high end design, something that stands out and looks amazing. My logo is blush pink and black, for packaging i need no more than 3 colours, maybe gold if any other colour is used. A photo of a sample derma roller is attached below for an idea of what the product looks like, however my roller with have a clear handle with a black roller. The roller comes in a clear case, the box dimensions will need to be 16 cm long, 4 cm high, 4.5 cm wide.
ATTACHED ARE 2 SAMPLE BOXES AS AN EXAMPLE OF THE SIZE OF BOX REQUIRED!

Target Market(s)

25-50 year old women in the US

Colors
e667a6
000000
efefef

Requirements
Must have
• LOGO
• NAME OF PRODUCT- Cosmetic Derma Roller
• NEEDLE DEPTH- 0.25mm
• CAUTION- For personal use only, Do not use if allergic to metal, Do not use on open skin, wounds or active acne, sterilise roller before and after use.
Nice to have
• BENEFITS- Skin Rejuvenation, Collagen Induction Therapy, Increase product absorption, reduce acne scars and pigmentation
• FEATURES- 540 high quality titanium needles, ultra sharp needle tips, cross-line needle arrangement, ergonomic handle, anti slip grip,

```html
<!DOCTYPE html>
<html lang="en">
<head>
<meta charset="utf-8">
<title>Velvet Glow Co. – Cosmetic Derma Roller Box Dieline</title>
<link rel="stylesheet" href="https://fonts.googleapis.com/css2?family=Oswald:wght@300;400;500&display=swap">
<style>
  :root {
    --paper: #ffffff;
    --bleed: #ece5e5;
    --cutline: #b8b6b6;
    --panel-base: #f1ebea;
    --blush: #e8a49c;
    --leaf-brown: #5c3b31;
    --label-cream: #fdf7f2;
    --rose-gold: #d29a86;
    --rose-gold-light: #ecc6b6;
    --ink: #2b2220;
  }
  * { margin: 0; padding: 0; box-sizing: border-box; }
  html, body { width: 1200px; height: 1200px; overflow: hidden; background: var(--paper); }
  .canvas { position: relative; width: 1200px; height: 1200px; }
  .dieline { position: absolute; inset: 0; }

  .label {
    position: absolute;
    background: var(--label-cream);
    border: 2px solid var(--rose-gold);
    box-shadow: inset 0 0 0 1px var(--rose-gold-light);
    font-family: "Oswald", sans-serif;
    color: var(--ink);
  }
  .brand {
    display: flex; align-items: center; justify-content: center; gap: 5px;
    font-family: "Oswald", sans-serif; font-weight: 400;
    color: var(--ink); letter-spacing: 0.12em; text-transform: uppercase;
  }
  .brand-mark { border: 1px solid var(--ink); display: inline-block; }
  .product-name {
    text-align: center; font-weight: 400; color: var(--rose-gold);
    letter-spacing: 0.02em; text-transform: uppercase;
  }

  .label--side { left: 226px; top: 422px; width: 172px; height: 356px; padding: 40px 14px 0; }
  .label--side .brand { font-size: 10px; margin-bottom: 52px; }
  .label--side .brand-mark { width: 10px; height: 10px; }
  .label--side .product-name { font-size: 13px; margin-bottom: 24px; }
  .info-list { list-style: none; font-size: 7.2px; line-height: 10.2px; text-transform: uppercase; letter-spacing: 0.02em; }
  .info-list li::before { content: "• "; }
  .info-list + .info-list { margin-top: 10px; }
  .caution { margin-top: 10px; font-size: 7.2px; line-height: 10.2px; text-transform: uppercase; letter-spacing: 0.02em; }

  .label--front { left: 669px; top: 418px; width: 136px; height: 123px; padding: 22px 8px 0; }
  .label--front .brand { font-size: 9px; margin-bottom: 26px; }
  .label--front .brand-mark { width: 9px; height: 9px; }
  .label--front .product-name { font-size: 10.5px; margin-bottom: 8px; }
  .needle-depth { text-align: center; font-size: 6px; font-weight: 300; letter-spacing: 0.08em; color: var(--ink); }
</style>
</head>
<body>
<div class="canvas">
  <svg class="dieline" width="1200" height="1200" viewBox="0 0 1200 1200" xmlns="http://www.w3.org/2000/svg">
    <defs>
      <linearGradient id="floral-tones" x1="0" y1="0" x2="1" y2="1">
        <stop offset="0" stop-color="#ead6d2"/>
        <stop offset="0.45" stop-color="#c99a90"/>
        <stop offset="1" stop-color="#7a5448"/>
      </linearGradient>
      <linearGradient id="floral-tones-light" x1="0" y1="0" x2="0" y2="1">
        <stop offset="0" stop-color="#efe4e2"/>
        <stop offset="0.6" stop-color="#dcbdb6"/>
        <stop offset="1" stop-color="#b78c80"/>
      </linearGradient>
    </defs>

    <!-- bleed outline -->
    <g class="bleed" fill="var(--bleed)" stroke="var(--bleed)" stroke-width="16" stroke-linejoin="round">
      <path d="M204,318 L204,80 Q204,36 228,30 L394,30 Q418,36 418,80 L418,318 Z"/>
      <path d="M418,318 L418,290 L440,270 L440,186 Q440,174 452,174 L600,174 Q612,174 612,186 L612,270 L630,290 L630,318 Z"/>
      <path d="M842,318 L842,290 L864,270 L864,186 Q864,174 876,174 L1022,174 Q1034,174 1034,186 L1034,270 L1052,290 L1052,318 Z"/>
      <path d="M204,318 L148,330 L148,870 L204,882 Z"/>
      <rect x="204" y="318" width="848" height="564"/>
      <path d="M418,882 L418,910 L440,930 L440,1020 Q440,1032 452,1032 L600,1032 Q612,1032 612,1020 L612,930 L630,910 L630,882 Z"/>
      <path d="M842,882 L842,910 L864,930 L864,1020 Q864,1032 876,1032 L1022,1032 Q1034,1032 1034,1020 L1034,930 L1052,910 L1052,882 Z"/>
      <path d="M630,882 L630,1120 Q630,1162 654,1168 L818,1168 Q842,1162 842,1120 L842,882 Z"/>
    </g>

    <!-- blank flaps -->
    <g class="blank-flaps" fill="var(--bleed)" stroke="var(--cutline)" stroke-width="1.2">
      <path d="M418,318 L418,290 L440,270 L440,186 Q440,174 452,174 L600,174 Q612,174 612,186 L612,270 L630,290 L630,318"/>
      <path d="M842,318 L842,290 L864,270 L864,186 Q864,174 876,174 L1022,174 Q1034,174 1034,186 L1034,270 L1052,290 L1052,318"/>
      <path d="M204,318 L148,330 L148,870 L204,882"/>
      <path d="M418,882 L418,910 L440,930 L440,1020 Q440,1032 452,1032 L600,1032 Q612,1032 612,1020 L612,930 L630,910 L630,882"/>
      <path d="M842,882 L842,910 L864,930 L864,1020 Q864,1032 876,1032 L1022,1032 Q1034,1032 1034,1020 L1034,930 L1052,910 L1052,882"/>
    </g>

    <!-- printed artwork areas -->
    <path class="artwork artwork--top-tuck" role="img" aria-label="Engraved floral illustration: blush pink wild roses, dark brown leaves and grey baroque scrolls"
          d="M204,318 L204,80 Q204,36 228,30 L394,30 Q418,36 418,80 L418,318 Z" fill="url(#floral-tones)"/>
    <rect class="artwork artwork--side-panel" role="img" aria-label="Engraved floral illustration with pink roses, brown leaves and grey scrolls behind the information label"
          x="204" y="318" width="214" height="564" fill="url(#floral-tones)"/>
    <rect class="artwork artwork--back-panel" role="img" aria-label="Scattered blush pink roses and brown leaf sprigs on pale blush background"
          x="418" y="318" width="212" height="564" fill="url(#floral-tones-light)"/>
    <rect class="artwork artwork--front-panel" role="img" aria-label="Dense bouquet of pink wild roses, rosebuds, dark brown leaves and grey baroque scrolls"
          x="630" y="318" width="212" height="564" fill="url(#floral-tones)"/>
    <rect class="artwork artwork--side-panel-2" role="img" aria-label="Pink roses, brown leaves and grey scrolls on pale blush background"
          x="842" y="318" width="210" height="564" fill="url(#floral-tones-light)"/>
    <path class="artwork artwork--bottom-tuck" role="img" aria-label="Engraved floral illustration with a pink wild rose, brown leaves and grey scrolls"
          d="M630,882 L630,1120 Q630,1162 654,1168 L818,1168 Q842,1162 842,1120 L842,882 Z" fill="url(#floral-tones)"/>

    <!-- cut and fold lines -->
    <g class="cut-lines" fill="none" stroke="var(--cutline)" stroke-width="1.2">
      <path d="M204,318 L204,80 Q204,36 228,30 L394,30 Q418,36 418,80 L418,318"/>
      <path d="M630,882 L630,1120 Q630,1162 654,1168 L818,1168 Q842,1162 842,1120 L842,882"/>
      <rect x="204" y="318" width="848" height="564"/>
      <line x1="418" y1="318" x2="418" y2="882"/>
      <line x1="630" y1="318" x2="630" y2="882"/>
      <line x1="842" y1="318" x2="842" y2="882"/>
      <line x1="204" y1="80" x2="418" y2="80"/>
      <line x1="630" y1="1110" x2="842" y2="1110"/>
    </g>
  </svg>

  <section class="label label--side">
    <div class="brand"><span class="brand-mark"></span>Velvet Glow Co.</div>
    <h2 class="product-name">Cosmetic Derma Roller</h2>
    <ul class="info-list features">
      <li>540 high quality 0.25 mm titanium needles</li>
      <li>Ultra sharp needle tips</li>
      <li>Cross-line needle arrangement</li>
      <li>Ergonomic handle</li>
      <li>Anti slip grip</li>
    </ul>
    <ul class="info-list benefits">
      <li>Skin rejuvenation</li>
      <li>Collagen induction therapy</li>
      <li>Increased product absorption</li>
      <li>Reduces acne scars and pigmentation</li>
    </ul>
    <p class="caution">Caution:<br>For personal use only<br>Do not use if allergic to metal<br>Avoid using on skin, wounds or active acne<br>Sterilize the roller prior to and after using</p>
  </section>

  <section class="label label--front">
    <div class="brand"><span class="brand-mark"></span>Velvet Glow Co.</div>
    <h1 class="product-name">Cosmetic Derma Roller</h1>
    <p class="needle-depth">0.25 MM</p>
  </section>
</div>
</body>
</html>
```